design a web site for equipment and software pos company

We would a web site similar to the site we whited labed our rtil system .https://tryplimvo.com/
website would be on RkTillDepot.com
we would a contact page
877-555-0142

We do not want an exact copy just something similar .
we are tablet po system

we are at

we are selling hardware and software

rk till depot
41 fernhollow ln
warren, nj 07318
we are cloud based system

Target Market(s)

any retail merchant

Industry/Entity Type

credit card processing in POS asystems

Coding

Coded - Design and coding required

Number of Pages Required

5+ page

Requirements
Must have
• be able to connect hostwren hosting
Nice to have
• modern looking site
Should not have
• any red

```html
<!DOCTYPE html>
<html lang="en">
<head>
<meta charset="utf-8">
<title>Rk Till Depot — Cloud POS</title>
<link href="https://fonts.googleapis.com/css2?family=Marcellus&family=Nunito+Sans:wght@400;600;700;800&family=Montserrat:wght@700;800&display=swap" rel="stylesheet">
<style>
:root{
  --ink:#1e1e1e;
  --dark:#202020;
  --yellow:#f6c416;
  --white:#ffffff;
  --grey-text:#666;
  --soft:#e6e6e6;
  --pale:#f1f4f6;
  --c1:#f6c416;--c2:#f2703d;--c3:#2fd6f2;--c4:#2ad0ea;--c5:#2f8ef0;--c6:#d437e2;
}
*{box-sizing:border-box;margin:0;padding:0}
html,body{width:1200px;height:4412px;overflow:hidden}
body{position:relative;background:var(--white);font-family:"Nunito Sans",sans-serif;color:var(--ink)}
.abs{position:absolute}
.bg{position:absolute;left:0;top:0}
.heading{font-family:"Marcellus",serif;font-weight:400}
.btn{position:absolute;background:var(--yellow);color:var(--ink);font-family:"Montserrat",sans-serif;font-weight:700;font-size:12px;display:flex;align-items:center;justify-content:center;letter-spacing:.3px}
.ph{position:absolute}

/* header */
.logo{left:70px;top:24px;color:var(--white);font-family:"Marcellus",serif;font-size:28px;display:flex;align-items:center;gap:10px}
.logo-mark{width:14px;height:14px;background:var(--yellow)}
.nav{top:32px;left:0;color:var(--white);font-size:13px;font-weight:600}
.nav span{position:absolute;white-space:nowrap}
.hero-kicker{left:70px;top:222px;color:var(--white);font-size:46px}
.hero-title{left:70px;top:276px;color:var(--white);font-family:"Montserrat",sans-serif;font-weight:800;font-size:56px;letter-spacing:1px}
.hero-sub{left:70px;top:356px;color:var(--white);font-size:23px;font-weight:600;line-height:33px}

/* about */
.sec-title{left:0;width:1200px;text-align:center;font-size:42px}
.sec-sub{left:0;width:1200px;text-align:center;font-size:14.5px;color:#333}
.about-item{width:240px;text-align:center}
.about-item .icon{width:62px;height:62px;margin:0 auto;border-radius:10px}
.about-item h3{margin-top:30px;font-size:14.5px;font-weight:700}
.about-item p{margin-top:22px;font-size:12.5px;line-height:22px;color:var(--grey-text)}

/* features */
.feat-title{color:var(--white)}
.pill{position:absolute;width:150px;height:89px;border-radius:45px;display:flex;align-items:center;color:var(--white);font-family:"Montserrat",sans-serif;font-weight:800;font-size:36px}
.pill .disc{width:80px;height:80px;border-radius:50%;background:var(--white);display:flex;align-items:center;justify-content:center;border:3px solid;flex:none}
.pill.l{justify-content:space-between;padding-left:18px;padding-right:5px}
.pill.r{justify-content:space-between;padding-left:5px;padding-right:18px}
.feat-text{color:var(--white);width:175px}
.feat-text h4{font-size:18px;font-weight:600;line-height:25px}
.feat-text p{font-size:12.5px;line-height:22px;color:#ddd;margin-top:2px}
.feat-text.left{text-align:right}

/* solutions */
.tile{position:absolute;width:170px;height:159px;overflow:hidden}
.tile .ph{inset:0}
.tile span{position:absolute;left:0;right:0;top:50%;transform:translateY(-50%);text-align:center;color:var(--white);font-size:16px;font-weight:600;line-height:21px}

/* partners */
.partner-title{left:70px;top:2666px;color:var(--white);font-size:40px}
.partner-text{left:70px;top:2724px;width:500px;color:#ddd;font-size:13px;line-height:24px}
.pcell{position:absolute;width:164px;height:97px;display:flex;align-items:center;justify-content:center}
.badge{background:#3a3a3a;border-radius:6px}

/* white label */
.wl-title{left:642px;top:2980px;font-size:42px;line-height:55px}
.wl-text{left:642px;top:3100px;width:430px;font-size:13px;line-height:23px;color:var(--grey-text)}

/* testimonials */
.card{position:absolute;top:3544px;width:337px;height:171px;background:var(--white);box-shadow:0 2px 14px rgba(0,0,0,.09);text-align:center}
.card h5{margin-top:52px;font-size:14px;font-weight:600}
.stars{margin-top:4px;color:var(--yellow);font-size:13px;letter-spacing:2px}
.card p{margin:10px 50px 0;font-size:12px;line-height:19px;color:var(--grey-text)}
.avatar{position:absolute;top:-42px;left:129px;width:80px;height:80px;border-radius:50%;border:4px solid var(--yellow);background:radial-gradient(circle at 50% 40%,#caa07e,#4a3a30)}
.dot{position:absolute;top:3737px;width:8px;height:8px;border-radius:50%;background:var(--white);box-shadow:0 0 3px rgba(0,0,0,.3)}

/* cta + footer */
.cta-title{left:252px;top:3860px;color:var(--white);font-size:42px}
.cta-text{left:252px;top:3926px;color:var(--white);font-size:15px;line-height:24px}
.email{left:882px;top:3876px;width:245px;height:43px;background:var(--white);display:flex;align-items:center;justify-content:center;font-size:13px;color:#333}
.foot-col{top:4052px;color:var(--white)}
.foot-col h6{font-family:"Marcellus",serif;font-weight:400;font-size:16px}
.foot-col ul{list-style:none;margin-top:30px}
.foot-col li{font-size:12px;line-height:27.5px;color:#ddd}
.foot-rule{position:absolute;top:4086px;height:1px;background:#444}
.vsep{position:absolute;top:4102px;width:2px;height:160px;background:var(--yellow)}
.contact-row{position:absolute;left:882px;color:#ddd;font-size:12px;line-height:18px;display:flex;gap:16px}
.social{position:absolute;top:4255px;width:34px;height:34px;border-radius:50%;border:2px solid var(--white)}
.copy{left:0;width:1200px;top:4356px;text-align:center;color:#ddd;font-size:12px}
.copy b{color:var(--yellow);font-weight:400}
</style>
</head>
<body>

<svg class="bg" width="1200" height="4412" viewBox="0 0 1200 4412" aria-hidden="true">
  <defs>
    <linearGradient id="heroGrad" x1="0" y1="0" x2="1" y2="1">
      <stop offset="0" stop-color="#2a2a2a"/><stop offset="1" stop-color="#1c1c1c"/>
    </linearGradient>
  </defs>
  <polygon points="0,0 1200,0 1200,430 0,599" fill="url(#heroGrad)"/>
  <circle cx="1150" cy="2050" r="210" fill="var(--pale)"/>
  <circle cx="-40" cy="2340" r="280" fill="var(--soft)"/>
  <polygon points="0,1224 1200,1027 1200,1840 0,1960" fill="var(--dark)"/>
  <circle cx="599" cy="1507" r="262" fill="#d8d8d8"/>
  <circle cx="599" cy="1507" r="254" fill="var(--white)"/>
  <polygon points="0,2625 1200,2482 1200,2808 0,2948" fill="var(--dark)"/>
  <ellipse cx="380" cy="3160" rx="215" ry="195" fill="var(--soft)"/>
  <polygon points="0,3783 1200,3646 1200,4412 0,4412" fill="var(--dark)"/>
</svg>

<!-- header -->
<div class="abs logo"><span class="logo-mark"></span>Rk Till Depot</div>
<nav class="abs nav">
  <span style="left:471px">Features</span>
  <span style="left:555px">About</span>
  <span style="left:623px">Pricing</span>
  <span style="left:695px">Business Types</span>
  <span style="left:817px">Products</span>
  <span style="left:902px">White lebel</span>
</nav>
<div class="btn" style="left:991px;top:21px;width:136px;height:42px">SIGN UP FREE</div>

<h1 class="abs heading hero-kicker">Sophisticated Cloud</h1>
<div class="abs hero-title">RTIL SYSTEM</div>
<p class="abs hero-sub">For Restaurant,Retails,Bar,Bakery,<br>Food Court,Ice- Cream Etc.</p>
<div class="btn" style="left:70px;top:440px;width:136px;height:44px">GET FREE OFFER</div>
<div class="ph" role="img" aria-label="Tablet on a stand showing the point of sale ordering screen" style="left:640px;top:190px;width:490px;height:335px;border-radius:28px;background:linear-gradient(135deg,#3a3a3a,#151515 60%,#6b5a3a);transform:rotate(8deg)"></div>

<!-- about -->
<h2 class="abs heading sec-title" style="top:638px">About The Software</h2>
<p class="abs sec-sub" style="top:700px">Many desktop publishing packages and web page editors now use Lorem Ipsum as their default model text.</p>
<div class="abs about-item" style="left:73px;top:800px"><div class="icon" role="img" aria-label="Payment card icon" style="background:linear-gradient(135deg,#3d7fd8,#f6c416)"></div><h3>Free Card Processing</h3><p>It is a long established fact that a reader will be distracted by the readable content .</p></div>
<div class="abs about-item" style="left:344px;top:800px"><div class="icon" role="img" aria-label="Shopping cart icon" style="background:linear-gradient(135deg,#f6c416,#4caf50)"></div><h3>Ring Up Sales With Ease</h3><p>It is a long established fact that a reader will be distracted by the readable content .</p></div>
<div class="abs about-item" style="left:614px;top:800px"><div class="icon" role="img" aria-label="Clock icon" style="background:radial-gradient(circle,#fff 40%,#f6a416 42%)"></div><h3>Save Time On Business</h3><p>It is a long established fact that a reader will be distracted by the readable content .</p></div>
<div class="abs about-item" style="left:883px;top:800px"><div class="icon" role="img" aria-label="Bar chart icon" style="background:linear-gradient(90deg,#f2703d,#f6c416,#4caf50,#3d7fd8)"></div><h3>Access Your Data Anytime</h3><p>It is a long established fact that a reader will be distracted by the readable content.</p></div>

<!-- features -->
<h2 class="abs heading sec-title feat-title" style="top:1184px">Features</h2>
<div class="ph" role="img" aria-label="Touchscreen POS monitor displaying a menu" style="left:420px;top:1385px;width:300px;height:250px;border-radius:6px;background:linear-gradient(160deg,#3a3a3a,#1a1a1a 70%,#555)"></div>

<div class="pill l" style="left:300px;top:1286px;background:var(--c1)">01<span class="disc" style="border-color:var(--c1)"><svg width="38" height="38" viewBox="0 0 38 38" fill="none" stroke="#333" stroke-width="2"><polyline points="4,30 14,18 22,24 34,8"/><circle cx="26" cy="28" r="6"/></svg></span></div>
<div class="pill l" style="left:265px;top:1449px;background:var(--c2)">02<span class="disc" style="border-color:var(--c2)"><svg width="38" height="38" viewBox="0 0 38 38" fill="none" stroke="#333" stroke-width="2"><rect x="4" y="9" width="30" height="20" rx="3"/><line x1="4" y1="15" x2="34" y2="15"/></svg></span></div>
<div class="pill l" style="left:288px;top:1613px;background:var(--c3)">03<span class="disc" style="border-color:var(--c3)"><svg width="38" height="38" viewBox="0 0 38 38" fill="none" stroke="#333" stroke-width="2"><rect x="5" y="8" width="22" height="24" rx="2"/><circle cx="27" cy="14" r="6"/></svg></span></div>
<div class="pill r" style="left:753px;top:1286px;background:var(--c4)"><span class="disc" style="border-color:var(--c4)"><svg width="38" height="38" viewBox="0 0 38 38" fill="none" stroke="#333" stroke-width="2"><circle cx="14" cy="12" r="8"/><line x1="20" y1="34" x2="20" y2="24"/><line x1="26" y1="34" x2="26" y2="18"/><line x1="32" y1="34" x2="32" y2="12"/></svg></span>04</div>
<div class="pill r" style="left:745px;top:1456px;background:var(--c5)"><span class="disc" style="border-color:var(--c5)"><svg width="38" height="38" viewBox="0 0 38 38" fill="none" stroke="#333" stroke-width="2"><circle cx="19" cy="19" r="14"/><circle cx="12" cy="17" r="3"/><circle cx="19" cy="14" r="3"/><circle cx="26" cy="17" r="3"/></svg></span>05</div>
<div class="pill r" style="left:753px;top:1627px;background:var(--c6)"><span class="disc" style="border-color:var(--c6)"><svg width="38" height="38" viewBox="0 0 38 38" fill="none" stroke="#333" stroke-width="2"><circle cx="19" cy="19" r="5"/><circle cx="19" cy="5" r="3"/><circle cx="19" cy="33" r="3"/><circle cx="6" cy="12" r="3"/><circle cx="32" cy="12" r="3"/><circle cx="6" cy="26" r="3"/><circle cx="32" cy="26" r="3"/></svg></span>06</div>

<div class="abs feat-text left" style="left:75px;top:1284px"><h4>Point Of Sale</h4><p>It is a long established fact that a reader will be distracted</p></div>
<div class="abs feat-text left" style="left:67px;top:1450px"><h4>Payments</h4><p>It is a long established fact that a reader will be distracted</p></div>
<div class="abs feat-text left" style="left:67px;top:1612px"><h4>Inventory</h4><p>It is a long established fact that a reader will be distracted.</p></div>
<div class="abs feat-text" style="left:948px;top:1284px"><h4>Sales Analytics</h4><p>It is a long established fact that a reader will be distracted</p></div>
<div class="abs feat-text" style="left:948px;top:1453px"><h4>Employee<br>Management</h4><p>It is a long established fact that a reader will be distracted</p></div>
<div class="abs feat-text" style="left:948px;top:1624px"><h4>Multi-store<br>Management</h4><p>It is a long established fact that a reader will be distracted</p></div>
<div class="btn" style="left:532px;top:1759px;width:136px;height:40px">VIEW ALL</div>

<!-- solutions -->
<h2 class="abs heading sec-title" style="top:1946px">Our Solution</h2>
<p class="abs sec-sub" style="top:2013px">Many desktop publishing packages and web page editors now use Lorem Ipsum as their default model text</p>
<div class="tile" style="left:160px;top:2060px"><div class="ph" role="img" aria-label="Restaurant interior with staff" style="background:linear-gradient(150deg,#8a7a66,#3d342c)"></div><span>Restaurant<br>POS</span></div>
<div class="tile" style="left:337px;top:2060px"><div class="ph" role="img" aria-label="Phone showing a pizza order over a pizza" style="background:linear-gradient(150deg,#a0633a,#4a2e1c)"></div><span>Pizzeria<br>POS</span></div>
<div class="tile" style="left:515px;top:2060px"><div class="ph" role="img" aria-label="Coffee shop counter with barista" style="background:linear-gradient(150deg,#6d6a68,#2c2a28)"></div><span>Coffee Shop<br>POS</span></div>
<div class="tile" style="left:692px;top:2060px"><div class="ph" role="img" aria-label="Bartender behind a bar" style="background:linear-gradient(150deg,#6a3c32,#2a1c1a)"></div><span>Bar<br>POS</span></div>
<div class="tile" style="left:870px;top:2060px"><div class="ph" role="img" aria-label="Hair salon stylist" style="background:linear-gradient(150deg,#7f8b99,#3b4450)"></div><span>Hair Salon<br>POS</span></div>
<div class="tile" style="left:160px;top:2227px"><div class="ph" role="img" aria-label="Food truck service window" style="background:linear-gradient(150deg,#7d6a58,#3a3028)"></div><span>Food Truck<br>POS</span></div>
<div class="tile" style="left:337px;top:2227px"><div class="ph" role="img" aria-label="Bakery display counter" style="background:linear-gradient(150deg,#8a7860,#3e3428)"></div><span>Bakery<br>POS</span></div>
<div class="tile" style="left:515px;top:2227px"><div class="ph" role="img" aria-label="Vape shop clerk" style="background:linear-gradient(150deg,#6f6f6f,#2e2e2e)"></div><span>Vape Shop<br>POS</span></div>
<div class="tile" style="left:692px;top:2227px"><div class="ph" role="img" aria-label="Retail checkout with card terminal" style="background:linear-gradient(150deg,#7a5a58,#2e2424)"></div><span>Retail Store<br>POS</span></div>
<div class="tile" style="left:870px;top:2227px"><div class="ph" role="img" aria-label="Fine dining waiter with tablet" style="background:linear-gradient(150deg,#5e7a70,#26332e)"></div><span>Fine Dinning<br>POS</span></div>
<div class="btn" style="left:532px;top:2423px;width:136px;height:40px">MORE SOLUTION</div>

<!-- partners -->
<h2 class="abs heading partner-title">Our Partners</h2>
<p class="abs partner-text">It is a long established fact that a reader will be distracted by the readable content of a page when looking at its layout.</p>
<div class="btn" style="left:70px;top:2795px;width:136px;height:42px">VIEW ALL</div>
<svg class="abs" style="left:630px;top:2606px" width="494" height="194" aria-hidden="true">
  <line x1="153" y1="0" x2="153" y2="194" stroke="#444"/>
  <line x1="337" y1="0" x2="337" y2="194" stroke="#444"/>
  <line x1="0" y1="97" x2="494" y2="97" stroke="#444"/>
</svg>
<div class="pcell" style="left:630px;top:2606px"><div class="badge" style="width:110px;height:30px"></div></div>
<div class="pcell" style="left:787px;top:2606px"><div class="badge" style="width:90px;height:22px;border-radius:50%"></div></div>
<div class="pcell" style="left:963px;top:2606px"><div class="badge" style="width:70px;height:36px"></div></div>
<div class="pcell" style="left:630px;top:2703px"><div class="badge" style="width:100px;height:28px"></div></div>
<div class="pcell" style="left:787px;top:2703px"><div class="badge" style="width:90px;height:18px"></div></div>
<div class="pcell" style="left:963px;top:2703px"><div class="badge" style="width:106px;height:30px"></div></div>

<!-- white label -->
<div class="ph" role="img" aria-label="POS terminal with receipt printer, cash drawer and card reader" style="left:135px;top:3030px;width:390px;height:330px;border-radius:14px;background:linear-gradient(160deg,#3c3c3c,#111 70%,#4a4a4a)"></div>
<h2 class="abs heading wl-title">A True White<br>Label POS System!</h2>
<p class="abs wl-text">It is a long established fact that a reader will be distracted by the readable content of a page when looking at its layout. The point of using Lorem Ipsum is that it has a more-or-less normal distribution of letters, as opposed to using 'Content here, content here', making it look like readable English. Many desktop publishing packages and web page .</p>
<div class="btn" style="left:644px;top:3264px;width:134px;height:42px">GET STARTED</div>

<!-- testimonials -->
<h2 class="abs heading sec-title" style="top:3415px">Testimonial</h2>
<div class="card" style="left:70px"><div class="avatar" role="img" aria-label="Customer portrait"></div><h5>The Brookfield Catering, UK</h5><div class="stars">★★★★★</div><p>“ It is a long established fact that a reader will be distracted by the readable content of a page when looking . ”</p></div>
<div class="card" style="left:431px"><div class="avatar" role="img" aria-label="Customer portrait"></div><h5>The Brookfield Catering, UK</h5><div class="stars">★★★★★</div><p>“ It is a long established fact that a reader will be distracted by the readable content of a page when looking . ”</p></div>
<div class="card" style="left:791px"><div class="avatar" role="img" aria-label="Customer portrait"></div><h5>The Brookfield Catering, UK</h5><div class="stars">★★★★★</div><p>“ It is a long established fact that a reader will be distracted by the readable content of a page when looking . ”</p></div>
<span class="dot" style="left:576px"></span><span class="dot" style="left:596px;background:var(--yellow)"></span><span class="dot" style="left:616px"></span>

<!-- cta -->
<div class="abs" style="left:72px;top:3835px;width:156px;height:156px;border-radius:50%;border:2px solid var(--white)"></div>
<div class="ph" role="img" aria-label="Handshake illustration" style="left:108px;top:3876px;width:84px;height:74px;border-radius:40%;background:linear-gradient(135deg,#f3b49a,#f2703d)"></div>
<h2 class="abs heading cta-title">Grow Your Business With RTIL</h2>
<p class="abs cta-text">If you would like to serve local businesses and help them implement<br>software and hardware retail solutions, fill out the partnership form.</p>
<div class="abs email">Enter Your Mail Id</div>
<div class="btn" style="left:882px;top:3929px;width:245px;height:40px">SUBSCRIBE NEWSLETTER</div>

<!-- footer -->
<div class="foot-rule" style="left:70px;width:1057px"></div>
<div class="abs foot-col" style="left:70px"><h6>Features</h6><ul><li>Point of Sale</li><li>Store Management</li><li>Menus &amp; Modifiers</li><li>Checkout</li><li>Customer Loyalty</li><li>Inventory</li></ul></div>
<div class="abs foot-col" style="left:318px"><h6>Solutions</h6><ul><li>Bakery POS</li><li>Bar POS</li><li>Coffee Shop POS</li><li>Food Truck POS</li><li>Liquor Store POS</li><li>Quick Service Restaurant POS</li></ul></div>
<div class="abs foot-col" style="left:627px"><h6>Products</h6><ul><li>Loyalty Hub</li><li>Back Office</li><li>Dashboard</li><li>Kitchen Display</li><li>Customer Display</li><li>Employee Management</li></ul></div>
<div class="abs foot-col" style="left:882px"><h6>Contact Us</h6></div>
<span class="vsep" style="left:245px"></span><span class="vsep" style="left:553px"></span><span class="vsep" style="left:817px"></span>

<div class="contact-row" style="top:4104px"><svg width="12" height="16" viewBox="0 0 12 16"><path d="M6 0a6 6 0 0 1 6 6c0 4-6 10-6 10S0 10 0 6a6 6 0 0 1 6-6z" fill="#fff"/><circle cx="6" cy="6" r="2" fill="#202020"/></svg><span style="margin-left:6px">41 Fernhollow Ln, Warren,<br>NJ 07318</span></div>
<div class="contact-row" style="top:4166px"><svg width="14" height="14" viewBox="0 0 14 14"><path d="M3 0l3 3-2 2c1 2 3 4 5 5l2-2 3 3-2 3C6 14 0 8 0 3z" fill="#fff"/></svg><span style="margin-left:4px">Phone: 877-555-0142</span></div>
<div class="contact-row" style="top:4206px"><svg width="14" height="10" viewBox="0 0 14 10"><rect width="14" height="10" fill="#fff"/><polyline points="0,0 7,6 14,0" fill="none" stroke="#202020"/></svg><span style="margin-left:4px">contact@rtilmail.com</span></div>
<div class="contact-row" style="top:4263px">Follow :</div>
<span class="social" style="left:955px"></span><span class="social" style="left:1000px"></span><span class="social" style="left:1045px"></span><span class="social" style="left:1090px"></span>

<p class="abs copy">© 2021 <b>RTIL</b>. All Rights Reserved</p>

</body>
</html>
```